Construction Website Design for Wordpress

Update:
I like this theme as a starting point. It seems like a very good start. Fonts, colors, motion, etc. https://advisory.kelbrowthemes.com/
***************************************************************************************

I want a new website design that can be implemented in wordpress. Here is my existing site: www.vantornmeasures.com
Attached is a document with the copy, requirements, sample images, etc. Let me know what questions you have.

Here is a sample of the info, but review the attached document for everything:

Website layout:
Title Bar
• Home
• Expertise
• Takeoffs
• Divisions Serviced (redesign from orig page: (http://www.vantornmeasures.com/scope-list/)
• Member Login
Requirements
• Home page has a slider with 3 dimmed commercial construction images and copy overlay
• Request for Proposal Form should be over the slider and the same look and location on every page.
• “Request For Proposal” – No Obligation
o Company Name
o Contact Name
o Contact Phone
o Contact Email
• Use the copy below for the pages
• Split the Client Testimonials among the pages

Target Market(s)

B2B - Construction Companies

Industry/Entity Type

Construction

Number of Pages Required

4 page

Font styles to use
Serif

Colors
0255a3
3276b5
85abd2
d0dfed

Requirements
Must have
• Construction images in slider
• Request for proposal form
• testimonials

```html
<!DOCTYPE html>
<html lang="en">
<head>
<meta charset="utf-8">
<title>Vantorn Measures — Construction Takeoff Experts</title>
<link rel="stylesheet" href="https://fonts.googleapis.com/css2?family=Montserrat:wght@300;400;500;600;700&family=Cormorant+Garamond:ital,wght@1,500&display=swap">
<style>
:root{
  --blue:#0255a3;
  --blue-mid:#3276b5;
  --blue-soft:#85abd2;
  --blue-pale:#d0dfed;
  --ink:#1d2b3a;
  --muted:#6b7785;
  --line:#e3e8ee;
  --paper:#ffffff;
  --mist:#f3f5f8;
  --dark:#231f20;
}
*{box-sizing:border-box;margin:0;padding:0}
html,body{width:1200px;height:3905px;overflow:hidden}
body{font-family:"Montserrat",sans-serif;color:var(--ink);background:var(--paper);position:relative}
section,header,footer{position:absolute;left:0;width:1200px}

/* top bar */
.topbar{top:0;height:34px;background:var(--mist);font-size:11px;color:var(--muted)}
.topbar .welcome{position:absolute;left:120px;top:11px}
.topbar .phone{position:absolute;right:150px;top:11px;color:var(--ink);font-weight:600}
.topbar .social{position:absolute;right:118px;top:6px;width:22px;height:22px;border-radius:50%;background:var(--blue)}

/* header */
.site-header{top:34px;height:83px;background:var(--paper);border-bottom:1px solid var(--line)}
.brand{position:absolute;left:120px;top:20px;color:var(--blue);font-weight:600;font-size:24px;letter-spacing:.5px;line-height:1}
.brand small{display:block;font-size:10.5px;letter-spacing:1.6px;margin-top:6px}
.nav{position:absolute;left:508px;top:34px;display:flex;gap:38px;font-size:12.5px;font-weight:500}
.nav a{color:var(--ink);text-decoration:none}
.nav a.active{color:var(--blue-mid)}
.member-btn{position:absolute;right:120px;top:24px;height:36px;width:146px;border:2px solid var(--blue);border-top:none;border-left:none;font-size:12px;font-weight:500;color:var(--blue);display:flex;align-items:center;justify-content:center;gap:8px}

/* hero */
.hero{top:117px;height:483px;background:linear-gradient(100deg,#8fa3b4 0%,#c9b9a2 35%,#e7c89c 60%,#f5dcc0 85%,#fbe9d4 100%);overflow:hidden}
.hero-photo{position:absolute;inset:0;background:radial-gradient(ellipse at 48% 40%,rgba(240,180,70,.55),rgba(0,0,0,0) 45%),linear-gradient(180deg,rgba(255,255,255,0) 60%,rgba(210,180,150,.6) 100%)}
.hero-copy{position:absolute;left:128px;top:117px;color:#fff}
.hero-copy .eyebrow{font-size:17px;color:var(--ink);opacity:.75}
.hero-copy h1{font-weight:300;font-size:46px;line-height:1.22;color:var(--blue);margin-top:14px}
.hero-copy p{font-weight:700;font-size:27px;line-height:1.3;color:var(--blue);margin-top:22px}

.rfp{position:absolute;left:807px;top:73px;width:260px;height:305px;background:rgba(255,255,255,.92)}
.rfp-tab{position:absolute;left:-2px;top:-10px;width:264px;height:66px;background:var(--blue-mid);color:#fff;text-align:center;padding-top:14px;font-size:14px;font-weight:500;clip-path:polygon(0 0,100% 0,100% 78%,50% 100%,0 78%)}
.rfp-tab small{display:block;font-size:11px;font-weight:600;margin-top:3px}
.rfp form{position:absolute;left:34px;top:78px;width:192px}
.rfp .field{height:28px;border:1px solid var(--blue-pale);background:#fff;font-size:10px;color:var(--muted);padding:8px 8px;margin-bottom:14px}
.rfp .send{width:110px;height:26px;margin:6px auto 0;background:#4fa8e0;color:#fff;font-size:10px;font-weight:600;display:flex;align-items:center;justify-content:center;letter-spacing:1px}

/* testimonials */
.testimonials{top:600px;height:480px;background:var(--blue);color:#fff;text-align:center}
.testimonials h2{font-weight:300;font-size:38px;margin-top:57px}
.testimonials h2 b{font-weight:700}
.quote-mark{margin:24px auto 0;display:block}
.testimonials blockquote{font-family:"Cormorant Garamond",serif;font-style:italic;font-weight:500;font-size:19px;line-height:1.55;width:640px;margin:22px auto 0}
.testimonials .author{font-size:13px;font-weight:600;margin-top:32px}
.testimonials .company{font-size:10.5px;opacity:.8;margin-top:2px}
.dots{display:flex;gap:8px;justify-content:center;margin-top:44px}
.dots span{width:11px;height:11px;border:1.5px solid var(--blue-soft);border-radius:50%}

/* scopes */
.scopes{top:1080px;height:638px;background:var(--paper)}
.scopes-intro{position:absolute;left:120px;top:158px;width:300px}
.scopes-intro h2{font-weight:400;font-size:36px;color:var(--blue);line-height:1.2}
.scopes-intro h2 b{font-weight:700}
.scopes-intro p{font-size:11.5px;line-height:1.6;color:var(--muted);margin-top:26px;border-left:1px solid var(--blue-pale);padding-left:16px;width:285px}
.btn-frame{display:inline-flex;align-items:center;justify-content:center;gap:8px;height:34px;border:2px solid var(--blue);border-top:none;border-right:none;font-size:11px;font-weight:500;color:var(--blue)}
.scopes-intro .btn-frame{width:130px;margin-top:30px}
.tile{position:absolute;width:281px;overflow:hidden}
.tile .fill{position:absolute;inset:0}
.tile span{position:absolute;left:22px;bottom:20px;color:#fff;font-weight:600;font-size:15px}
.tile.active .fill{background:linear-gradient(160deg,#3e6f9e,#1a4f86)}
.tile.active{background:var(--blue)}
.tile.active h3{position:absolute;left:22px;top:28px;color:#fff;font-size:16px;font-weight:600}
.tile.active p{position:absolute;left:22px;top:60px;width:230px;color:#dfe9f4;font-size:11px;line-height:1.5}
.tile.active svg{position:absolute;left:22px;bottom:22px}

/* success */
.success{top:1718px;height:482px;background:linear-gradient(180deg,#e9ecef,#f1f2f4 60%,#e7eaee);text-align:center}
.success h2{font-weight:400;font-size:36px;color:var(--blue);margin-top:90px}
.success h2 b{font-weight:700}
.stats{display:flex;justify-content:center;gap:62px;margin-top:34px}
.stat{width:160px}
.stat strong{display:block;font-size:38px;font-weight:700;color:var(--blue);margin-top:6px}
.stat small{font-size:14px;color:var(--muted);display:block;margin-top:6px}
.success .btn-frame{width:175px;margin-top:46px;background:#fff;border:2px solid var(--blue)}

/* services */
.services{top:2200px;height:364px;text-align:center}
.services h2{font-weight:400;font-size:36px;color:var(--blue);margin-top:76px}
.services h2 b{font-weight:700}
.services .lede{font-size:11.5px;color:var(--muted);margin-top:10px}
.service{position:absolute;top:210px;width:290px;text-align:left;display:flex;gap:16px}
.service .ic{width:58px;height:58px;flex:none;border-radius:50%;border:2px solid var(--blue);display:flex;align-items:center;justify-content:center}
.service .ic.solid{background:var(--blue)}
.service h3{font-size:15px;font-weight:400;color:var(--ink);margin-top:2px}
.service p{font-size:11px;line-height:1.55;color:var(--muted);margin-top:8px;width:200px}

/* many more */
.more{top:2564px;height:208px;background:var(--mist)}
.more h2{position:absolute;left:120px;top:60px;font-weight:400;font-size:34px;color:var(--blue)}
.more h2 b{font-weight:700}
.more p{position:absolute;left:120px;top:114px;width:640px;font-size:13px;color:var(--muted);line-height:1.5}
.more .btn-frame{position:absolute;left:903px;top:72px;width:177px;border:2px solid var(--blue);border-bottom:none;border-left-width:2px}

/* role */
.role{top:2772px;height:638px}
.role-photo{position:absolute;left:120px;top:78px;width:480px;height:477px;background:linear-gradient(180deg,#6fa4d8 0%,#a9c8e6 45%,#b69c6c 100%)}
.role-panel{position:absolute;left:600px;top:78px;width:480px;height:477px;background:var(--dark);color:#fff;padding:150px 42px 0}
.role-panel h2{font-weight:300;font-size:27px;line-height:1.25}
.role-panel h2 b{font-weight:700}
.role-panel p{font-size:13px;line-height:1.6;color:#cfd3d8;margin-top:28px}
.role-panel .btn-frame{width:128px;margin-top:32px;color:#fff;border-color:#fff;border-top:none;border-right:none}

/* footer */
.site-footer{top:3410px;height:495px;background:linear-gradient(160deg,#0a5aa6,#0255a3 55%,#2c6fb0);color:#fff}
.site-footer .brand{top:68px;color:#fff}
.footer-about{position:absolute;left:120px;top:130px;width:440px;font-size:12px;line-height:1.65}
.footer-about p+p{margin-top:20px}
.footer-about .btn-frame{width:128px;margin-top:44px;color:#fff;border-color:#fff;border-top:none;border-right:none}
.footer-col{position:absolute;top:80px}
.footer-col h4{font-size:16px;font-weight:500}
.footer-col ul{list-style:none;margin-top:34px;font-size:12.5px;line-height:2}
.links{left:632px}
.contact{left:838px}
.contact .call{font-size:19px;font-weight:400;margin-top:36px}
.contact .mail{font-size:12px;margin-top:4px}
.contact .social{width:38px;height:38px;border-radius:50%;border:2px solid #fff;margin-top:26px}
.cards{display:flex;gap:8px;margin-top:26px}
.cards span{width:42px;height:26px;background:#fff;border-radius:2px}
.cards span:nth-child(2){background:var(--blue-pale)}
.cards span:nth-child(4){background:var(--blue-soft)}
.copyright{position:absolute;left:0;right:0;bottom:26px;text-align:center;font-size:11.5px}
.copyright em{font-style:normal;color:var(--blue-soft)}
.copyright i{font-style:normal;margin:0 12px}
</style>
</head>
<body>

<div class="topbar" style="position:absolute;left:0;width:1200px">
  <span class="welcome">Welcome to Vantorn Measures</span>
  <span class="phone">&#9742; +1 555-014-2290</span>
  <span class="social"></span>
</div>

<header class="site-header">
  <div class="brand">VANTORN MEASURES<small>CONSTRUCTION TAKEOFF EXPERTS</small></div>
  <nav class="nav">
    <a class="active">Home</a><a>Expertise</a><a>Takeoffs</a><a>Divisions Serviced</a>
  </nav>
  <div class="member-btn">
    <svg width="13" height="13" viewBox="0 0 14 14"><circle cx="7" cy="4" r="3" fill="none" stroke="#0255a3" stroke-width="1.5"/><path d="M1 13c0-3 3-5 6-5s6 2 6 5" fill="none" stroke="#0255a3" stroke-width="1.5"/></svg>
    Member Login
  </div>
</header>

<section class="hero">
  <div class="hero-photo" role="img" aria-label="Dimmed photo of an excavator working on a construction site at sunset"></div>
  <div class="hero-copy">
    <div class="eyebrow">Time</div>
    <h1>In construction, beyond<br>your reputation,</h1>
    <p>Nothing is more valuable than<br>your time.</p>
  </div>
  <div class="rfp">
    <div class="rfp-tab">Request For Proposal<small>No Obligation</small></div>
    <form>
      <div class="field">Name</div>
      <div class="field">Company Name</div>
      <div class="field">Phone</div>
      <div class="field">Email</div>
      <div class="send">SEND</div>
    </form>
  </div>
</section>

<section class="testimonials">
  <h2>Words from <b>our Clients</b></h2>
  <svg class="quote-mark" width="54" height="42" viewBox="0 0 54 42"><path d="M0 42V22C0 9 7 2 20 0v8c-6 2-9 6-9 12h9v22zM30 42V22C30 9 37 2 50 0v8c-6 2-9 6-9 12h9v22z" fill="#85abd2"/></svg>
  <blockquote>Sometimes our work is super time sensitive and when I'm given unreasonable deadlines, Vantorn Measures is my secret weapon. They are realistic in their assessments and when I say go, they never fail to deliver just what I want, just the way I want it!</blockquote>
  <div class="author">Dara Whitcombe</div>
  <div class="company">Harbor Line Builders, LLC.</div>
  <div class="dots"><span></span><span></span><span></span><span></span></div>
</section>

<section class="scopes">
  <div class="scopes-intro">
    <h2>Expert Takeoffs<br>For All <b>Scopes</b></h2>
    <p>There are many variations of passages of Lorem Ipsum available, but the majority have suffered alteration in some form, by injected humour, or randomised words which don't look even slightly believable. If you are going to use a passage of Lorem Ipsum, you need to be sure there isn't anything ...</p>
    <div class="btn-frame">&rarr; View All</div>
  </div>
  <div class="tile" style="left:487px;top:78px;height:222px">
    <div class="fill" role="img" aria-label="Photo of a painter finishing a white porch railing" style="background:linear-gradient(180deg,#9fc0dc,#d8dadb 55%,#8a8d90)"></div>
    <span>Painting</span>
  </div>
  <div class="tile active" style="left:799px;top:78px;height:222px">
    <div class="fill" role="img" aria-label="Dimmed photo of a finished millwork office interior"></div>
    <h3>Millwork</h3>
    <p>Millwork is arguably one of the more refined and exacting scopes that we face.</p>
    <svg width="16" height="12" viewBox="0 0 16 12"><path d="M0 6h14M9 1l5 5-5 5" fill="none" stroke="#fff" stroke-width="1.6"/></svg>
  </div>
  <div class="tile" style="left:487px;top:333px;height:227px">
    <div class="fill" role="img" aria-label="Photo of roofers laying insulation boards on a flat roof" style="background:linear-gradient(180deg,#3d86c8,#7ab0dc 40%,#9a9da0 70%,#55585c)"></div>
    <span>Roofing - Siding</span>
  </div>
  <div class="tile" style="left:799px;top:333px;height:227px">
    <div class="fill" role="img" aria-label="Photo of workers finishing a concrete foundation slab" style="background:linear-gradient(180deg,#bfd6ea,#cfd0cc 45%,#a7a49c)"></div>
    <span>Concrete - Foundation</span>
  </div>
</section>

<section class="success" role="img" aria-label="Faded photo of a smiling business team behind the statistics">
  <h2>Our <b>Success Story</b></h2>
  <div class="stats">
    <div class="stat">
      <svg width="36" height="28" viewBox="0 0 36 28"><circle cx="12" cy="7" r="6" fill="#0255a3"/><circle cx="26" cy="8" r="5" fill="#0255a3"/><path d="M0 28c0-8 5-12 12-12s12 4 12 12zM22 16c7 0 14 3 14 12h-10c0-5-1-9-4-12z" fill="#0255a3"/></svg>
      <strong>100+</strong><small>Team Member</small>
    </div>
    <div class="stat">
      <svg width="34" height="30" viewBox="0 0 34 30"><rect x="3" y="2" width="28" height="28" fill="#0255a3"/><g fill="#e9ecef"><rect x="8" y="7" width="4" height="4"/><rect x="15" y="7" width="4" height="4"/><rect x="22" y="7" width="4" height="4"/><rect x="8" y="14" width="4" height="4"/><rect x="15" y="14" width="4" height="4"/><rect x="22" y="14" width="4" height="4"/><rect x="14" y="22" width="6" height="8"/></g></svg>
      <strong>300+</strong><small>Complete Project</small>
    </div>
    <div class="stat">
      <svg width="36" height="28" viewBox="0 0 36 28"><circle cx="12" cy="7" r="6" fill="#0255a3"/><circle cx="26" cy="8" r="5" fill="#0255a3"/><path d="M0 28c0-8 5-12 12-12s12 4 12 12zM22 16c7 0 14 3 14 12h-10c0-5-1-9-4-12z" fill="#0255a3"/></svg>
      <strong>1000</strong><small>Registered Users</small>
    </div>
    <div class="stat">
      <svg width="32" height="28" viewBox="0 0 32 28"><circle cx="16" cy="7" r="6" fill="#0255a3"/><path d="M3 28c0-8 6-12 13-12s13 4 13 12z" fill="#0255a3"/></svg>
      <strong>2000</strong><small>Happy Customers</small>
    </div>
  </div>
  <div class="btn-frame">&rarr; Request For Proposal</div>
</section>

<section class="services">
  <h2>Expert <b>Takeoffs</b></h2>
  <p class="lede">Construction is a complex, ever-changing challenge where seemingly no two days are the same</p>
  <div class="service" style="left:120px">
    <div class="ic"><svg width="24" height="24" viewBox="0 0 24 24"><path d="M4 20l2-6L16 4l4 4-10 10zM14 6l4 4" fill="none" stroke="#0255a3" stroke-width="1.8"/></svg></div>
    <div><h3>Request a Takeoff</h3><p>Construction is a complex, ever changing challenge where seemingly no ...</p></div>
  </div>
  <div class="service" style="left:440px">
    <div class="ic solid"><svg width="26" height="26" viewBox="0 0 26 26"><circle cx="11" cy="8" r="5" fill="none" stroke="#fff" stroke-width="1.8"/><path d="M2 24c0-6 4-9 9-9" fill="none" stroke="#fff" stroke-width="1.8"/><circle cx="19" cy="19" r="4" fill="none" stroke="#fff" stroke-width="1.8"/><path d="M19 13v2M19 23v2M13 19h2M23 19h2" stroke="#fff" stroke-width="1.8"/></svg></div>
    <div><h3>Account Management</h3><p>When a new client relationship is established, Vantorn Measures will work with ...</p></div>
  </div>
  <div class="service" style="left:760px">
    <div class="ic"><svg width="22" height="26" viewBox="0 0 22 26"><text x="11" y="20" text-anchor="middle" font-family="Montserrat,sans-serif" font-size="20" fill="#0255a3">$</text></svg></div>
    <div><h3>Benefits</h3><p>Time, money, and confidence combine to define the fundamental benefits ...</p></div>
  </div>
</section>

<section class="more">
  <h2>And <b>Many, Many,</b> More</h2>
  <p>Construction is a complex, ever-changing challenge where seemingly no two days are the same</p>
  <div class="btn-frame">&rarr; Request For Proposal</div>
</section>

<section class="role">
  <div class="role-photo" role="img" aria-label="Photo of a commercial building under construction wrapped in scaffolding"></div>
  <div class="role-panel">
    <h2>Vantorn <b>Measures</b> fills a<br><b>unique role</b> in the <b>commercial<br>construction</b> industry.</h2>
    <p>More than merely an asset to your business, we strive to become partners, mutually invested in success. Earning your trust will be a process but not a challenge.</p>
    <div class="btn-frame">&rarr; Explore More</div>
  </div>
</section>

<footer class="site-footer">
  <div class="brand">VANTORN MEASURES<small>CONSTRUCTION TAKEOFF EXPERTS</small></div>
  <div class="footer-about">
    <p>Dedicated to saving our clients time and money by specializing in accurate, reliable materials quantity calculations, Vantorn Measures allows general contractors to confidently propose on more work with less stress.</p>
    <p>To receive a no-obligation answer to your takeoff needs complete the Request for Proposal form ...</p>
    <div class="btn-frame">&rarr; Discover More</div>
  </div>
  <div class="footer-col links">
    <h4>Quick Links</h4>
    <ul><li>Home</li><li>Expertise</li><li>Takeoffs</li><li>Divisions Serviced</li><li>Contact Us</li></ul>
  </div>
  <div class="footer-col contact">
    <h4>Contact Us</h4>
    <div class="call">Call Us: +1 555-014-2290</div>
    <div class="mail">Email: info@vantornmeasures.com</div>
    <div class="social"></div>
    <div class="cards"><span></span><span></span><span></span><span></span></div>
  </div>
  <div class="copyright">© 2019 <em>Vantorn Measures</em>. All Rights Reserved.<i>|</i>Become a Member<i>|</i><em>Privacy Policy</em><i>|</i>Sitemap</div>
</footer>

</body>
</html>
```